I am a highly experienced private practice psychotherapist serving high end clientele in the Wall Street area of New York City. I need electronic letterhead (that can also be printed) to use for bills, receipts, and correspondences.

My clients are very high end and are used to elegance and wealth. The letterhead should contain the following information: Marian T. Holcombe, LCSW 72 Pellham Street, Suite 2561 New York, NY 10087 Phone : (917) 555-3194 email: therapy@marianholcombelcsw.example website: www.marianholcombelcsw.example

Thank you for your designs. Please be advised that the letterhead will be used for bills/invoices; professional letters to other mental health professionals and doctors, as well as to attorneys. It needs to be highly professional in the same way that a law firm has professional and elegant letterhead, raher than whimsical or with spa designers. My letters end up as official documents.

```html
<!DOCTYPE html>
<html lang="en">
<head>
<meta charset="utf-8">
<title>Marian T. Holcombe, LCSW — Letterhead</title>
<link rel="stylesheet" href="https://fonts.googleapis.com/css2?family=Lato:wght@400;700&display=swap">
<style>
  :root {
    --backdrop: #1c1714;
    --paper: #ffffff;
    --ink-name: #3a3a3a;
    --ink-detail: #6a6a6a;
    --plum: #7e1a86;
    --plum-detail: #8a2a92;
  }
  * { margin: 0; padding: 0; box-sizing: border-box; }
  html, body {
    width: 1200px;
    height: 837px;
    overflow: hidden;
    background: var(--backdrop);
  }
  .canvas {
    position: relative;
    width: 1200px;
    height: 837px;
    font-family: "Lato", Arial, sans-serif;
  }
  .sheet {
    position: absolute;
    top: 18px;
    width: 576px;
    height: 808px;
    background: var(--paper);
  }
  .sheet--mono { left: 13px; }
  .sheet--plum { left: 608px; }
  .letterhead-footer {
    position: absolute;
    left: 0;
    right: 0;
    top: 733px;
    text-align: center;
    font-size: 8.4px;
    letter-spacing: 0.1px;
  }
  .footer-name {
    font-size: 8.8px;
    font-weight: 700;
    line-height: 11px;
    margin-bottom: 6px;
  }
  .footer-name .credential { font-weight: 400; }
  .footer-line {
    line-height: 11px;
    margin-bottom: 6px;
  }
  .divider { margin: 0 7px; }
  .sheet--mono .footer-name { color: var(--ink-name); }
  .sheet--mono .footer-line { color: var(--ink-detail); }
  .sheet--plum .footer-name { color: var(--plum); }
  .sheet--plum .footer-name .credential { font-weight: 700; }
  .sheet--plum .footer-line { color: var(--plum-detail); }
</style>
</head>
<body>
<main class="canvas">
  <section class="sheet sheet--mono" aria-label="Letterhead, neutral grey version">
    <footer class="letterhead-footer">
      <p class="footer-name">Marian T. Holcombe<span class="credential">, LCSW</span></p>
      <p class="footer-line">therapy@marianholcombelcsw.example<span class="divider">|</span>www.marianholcombelcsw.example</p>
      <p class="footer-line">(917) 555-3194<span class="divider">|</span>72 Pellham Street, Suite 2561, New York, NY 10087</p>
    </footer>
  </section>

  <section class="sheet sheet--plum" aria-label="Letterhead, plum version">
    <footer class="letterhead-footer">
      <p class="footer-name">Marian T. Holcombe<span class="credential">, LCSW</span></p>
      <p class="footer-line">therapy@marianholcombelcsw.example<span class="divider">|</span>www.marianholcombelcsw.example</p>
      <p class="footer-line">(917) 555-3194<span class="divider">|</span>72 Pellham Street, Suite 2561, New York, NY 10087</p>
    </footer>
  </section>
</main>
</body>
</html>
```